Design marketing/advertisement email for consulting business

Hello - My company, Brindle-Oakes, is looking for a marketing professional to compose a "marketing" email to be sent to potential professional referral sources. The email should provide an introduction of our company's capabilities and services. We want this marketing piece to invite the recipient to schedule a call with us to further discuss how we could best work together. The email must included elements of our brand. Our website is www.brindleoakes-example.com and will provide you with all the details about our business as well as our logo, branding, contact details etc. Thanks so much!
Industry/Entity Type
Business

```html
<!DOCTYPE html>
<html lang="en">
<head>
<meta charset="utf-8">
<title>Brindle-Oakes – Senior Housing Consulting</title>
<link href="https://fonts.googleapis.com/css2?family=Arimo:wght@400&family=Crimson+Text:ital@1&display=swap" rel="stylesheet">
<style>
  :root {
    --backdrop: #ad9a74;
    --paper: #ffffff;
    --ink: #4a4652;
    --ink-dark: #111111;
    --accent: #e77c5c;
    --panel-grey: #c8c6c3;
    --bar-grey: #b5b5b5;
    --service-blue: #1a6fe0;
    --white: #ffffff;
  }
  * { box-sizing: border-box; margin: 0; padding: 0; }
  html, body { width: 1200px; height: 1200px; overflow: hidden; }
  body { background: var(--backdrop); font-family: "Arimo", Arial, sans-serif; }

  .flyer {
    position: absolute; left: 241px; top: 151px;
    width: 720px; height: 900px;
    background: var(--paper); overflow: hidden;
  }

  .brand {
    position: absolute; left: 38px; top: 36px;
    display: flex; align-items: center; gap: 14px;
  }
  .brand-square { width: 56px; height: 56px; background: var(--accent); }
  .brand-name { font-family: "Arimo", Arial, sans-serif; font-size: 36px; color: var(--ink); letter-spacing: 0.5px; }

  .intro {
    position: absolute; left: 30px; top: 142px; width: 402px;
    font-family: "Crimson Text", Georgia, serif; font-style: italic;
    font-size: 20.4px; line-height: 27.1px; color: var(--ink);
    text-align: justify; hyphens: auto;
    text-indent: 82px;
  }
  .intro .initial { font-size: 46px; line-height: 20px; }

  .contact-bar {
    position: absolute; height: 30px; background: var(--bar-grey);
    display: flex; align-items: center; justify-content: center; gap: 12px;
    font-size: 19px; color: var(--ink-dark);
  }
  .contact-bar svg { width: 26px; height: 22px; }
  .contact-phone { left: 29px; top: 562px; width: 194px; }
  .contact-fax { left: 241px; top: 562px; width: 196px; }
  .contact-email { left: 60px; top: 606px; width: 340px; font-size: 17px; }

  .services {
    position: absolute; left: 456px; top: 138px; width: 235px; height: 492px;
    background: var(--panel-grey); padding: 0 6px;
  }
  .services-title {
    height: 76px; display: flex; align-items: center; justify-content: center;
    font-size: 22px; color: var(--ink-dark); letter-spacing: 0.5px;
    padding-right: 10px;
  }
  .service {
    height: 132px; margin-bottom: 7px; background: var(--service-blue);
    color: var(--white); text-align: center;
    display: flex; flex-direction: column; justify-content: center; gap: 6px;
  }
  .service-name { font-size: 28px; }
  .service-detail { font-size: 16.5px; line-height: 21.5px; }

  .skyline {
    position: absolute; left: 44px; top: 684px; width: 676px; height: 216px;
    background:
      linear-gradient(180deg, rgba(255,255,255,1) 0%, rgba(226,240,238,0.8) 40%, rgba(180,200,205,0.9) 80%, rgba(140,140,150,0.9) 100%),
      linear-gradient(90deg, #ffffff 0%, #dceceb 30%, #cfdfe2 70%, #ffffff 100%);
  }

  .office {
    position: absolute; top: 673px;
    font-size: 16.5px; line-height: 21.6px; color: var(--ink-dark);
  }
  .office-austin { left: 42px; }
  .office-palo-alto { left: 384px; }
</style>
</head>
<body>
  <main class="flyer">
    <header class="brand">
      <span class="brand-square" aria-hidden="true"></span>
      <span class="brand-name">BrindleOakes</span>
    </header>

    <p class="intro"><span class="initial">B</span>rindle-Oakes was established to provide senior housing expertise to the real estate investment and development communities. Founded in 2011, Brindle-Oakes offers consulting services to investors, developers and asset managers within the senior housing investment space. Drawing upon the extensive experience of the company’s principals, Nora Brindle and Jane Oakes, Brindle-Oakes is able to offer a wide array of services to ensure successful and profitable senior housing development projects and investments. Brindle-Oakes has offices in Austin, Texas and Palo Alto, California.</p>

    <div class="contact-bar contact-phone">
      <svg viewBox="0 0 26 22" aria-hidden="true"><path d="M2 8 Q13 0 24 8 L21 11 L18 8 L8 8 L5 11 Z" fill="none" stroke="#111" stroke-width="1.5"/><rect x="6" y="11" width="14" height="9" fill="none" stroke="#111" stroke-width="1.5"/><circle cx="13" cy="15.5" r="2.2" fill="none" stroke="#111" stroke-width="1.3"/></svg>
      <span>512.555.0148</span>
    </div>
    <div class="contact-bar contact-fax">
      <svg viewBox="0 0 26 22" aria-hidden="true"><rect x="8" y="2" width="10" height="7" fill="none" stroke="#111" stroke-width="1.5"/><rect x="3" y="9" width="20" height="11" fill="none" stroke="#111" stroke-width="1.5"/><line x1="7" y1="13" x2="19" y2="13" stroke="#111" stroke-width="1.3"/><line x1="7" y1="16" x2="19" y2="16" stroke="#111" stroke-width="1.3"/></svg>
      <span>512.555.0192</span>
    </div>
    <div class="contact-bar contact-email">
      <svg viewBox="0 0 26 22" aria-hidden="true"><rect x="2" y="4" width="22" height="14" fill="none" stroke="#111" stroke-width="1.5"/><path d="M2 4 L13 12 L24 4" fill="none" stroke="#111" stroke-width="1.5"/></svg>
      <span>info@brindleoakes-example.com</span>
    </div>

    <aside class="services">
      <h2 class="services-title">SERVICES</h2>
      <div class="service">
        <span class="service-name">Development</span>
        <span class="service-detail">Acquisition, Planning<br>and Design</span>
      </div>
      <div class="service">
        <span class="service-name">Operation</span>
        <span class="service-detail">Audits and Assessments</span>
      </div>
      <div class="service">
        <span class="service-name">Disposition</span>
        <span class="service-detail">Transition and<br>Exit Strategies</span>
      </div>
    </aside>

    <div class="skyline" role="img" aria-label="Faded city skyline with towers under a pale sky"></div>

    <address class="office office-austin" style="font-style:normal">
      Brindle-Oakes Partners, LLC – Austin<br>
      1400 Cedar Row Blvd.<br>
      Suite 410-118<br>
      Austin, TX 78701
    </address>
    <address class="office office-palo-alto" style="font-style:normal">
      Brindle-Oakes Partners, LLC – Palo Alto<br>
      88 Linden Avenue, #20040<br>
      Palo Alto, CA 94301
    </address>
  </main>
</body>
</html>
```